New VPN Company needs a Web Site

This competition is the first step of a 3 step project.
- Step 1: (This project) We are looking to have 3 pages designed to evaluate your design and illustration skills.
- Step 2: Once we find a winner, we will request a bid to have the rest of the website designed.
- Step 3: We will request a bid to have the designs converted into WordPress if the bid is acceptable.
If you have the capabilities, Steps 2 and 3 can be combined into a single project/bid.
Design Notes
- Design type should be “FLAT.”
- Clean, crisp design that communicates security, anonymity, encryption, privacy.
- Please take a look at the following website: http://brisk.toveltunnel.com This is our current Word Press based setup. It contains all the link structures, menus, and text for the website. PLEASE NOTE THAT THE CURRENT DESIGN HAS NOTHING TO DO WITH WHAT YOU ARE DESIGNING. I USED THE FIRST WORD PRESS TEMPLATE THAT I COULD FIND. Once you submit a winning design, either YOU (if you have the skill set) or somebody else will take the designs and convert it into a word press template.
Here are a few of the pages from http://brisk.toveltunnel.com that I would like to see mockups for:
o Main Page: http://brisk.toveltunnel.com
Notes
• I have a dummy graphic up. That graphic needs to be replaced. Also as per the “Should have’s” I want all pages to have unlimited stretching right and left without that grey border on the right and left sides that are currently present.)
o Features Page: http://brisk.toveltunnel.com/index.php/features/
o Windows App download Page: http://brisk.toveltunnel.com/index.php/vpn-apps/vpn-for-windows/

- I want a “top bar” which shows Your IP: Your ISP: Your Location: Your Status: Like most of my competitors have.
- This website needs several original illustrations.
- The website must be clean, uncluttered, and concise.
- Use the copy provided from the http://brisk.toveltunnel.com website.
- Colors are up to the designers; this includes logo colors

- Please take a look at some of our competitor's websites for overall inspiration:
o https://www.quaywardnet.com
o https://bexilvpn.com
o https://www.tovrimesk.com/en-us/index
o https://www.dralmoxvpn.com/
o https://www.glenvixvpn.com/
o https://www.yorbalune.com/
o https://www.plumtavrikvpn.com/en_US/

Target Market(s)

Consumers between 18-30 from around the world.

Industry/Entity Type

Internet Service Provider

Number of Pages Required

3 page

Colors

Designer to choose colors to be used in the design.

Requirements
Must have
• - Look great on Desktop, Tablet, and smartphones.
• - The current template has borders. I want the new design to stretch with the browser, e.g., no grey borders on the left and right of the screen.
• - All illustration work must be original. We are not interested in stock photos.
• - Use attached logo. Font is Nexa Xbold.
Should not have
• - A nonfunctional look on smartphones. A high percentage of purchases will be made by smartphone users.
• - Should only have solid colors (two tone or three tone is ok). I am not a big fan of gradients or soft shadows.

```html
<!DOCTYPE html>
<html lang="en">
<head>
<meta charset="utf-8">
<title>Brisk VPN – Home</title>
<link href="https://fonts.googleapis.com/css2?family=Montserrat:wght@400;500;600;700&family=Tinos&display=swap" rel="stylesheet">
<style>
:root{
  --orange:#f9a100;
  --nav-grey:#787878;
  --light-grey:#ececec;
  --white:#ffffff;
  --ink:#1d1d1d;
  --footer:#243e3e;
  --green:#2eb24b;
  --cta-grey:#666666;
  --brand-red:#e8473b;
  --backdrop:#dcdcdc;
}
*{box-sizing:border-box;margin:0;padding:0}
html,body{width:1200px;height:1200px;overflow:hidden}
body{background:var(--backdrop);font-family:"Montserrat",sans-serif;color:var(--ink);position:relative}
.page{position:absolute;left:435px;top:10px;width:514px;height:1844px;transform:scale(.64);transform-origin:0 0;background:var(--white);overflow:hidden}
section,header,footer{position:relative;width:100%}

.nav{height:32px;background:var(--nav-grey);display:flex;align-items:center;justify-content:space-between;padding:0 16px 0 30px}
.brand{display:flex;align-items:center;gap:5px;color:var(--white);font-size:9px;font-weight:700;letter-spacing:.5px}
.brand-dot{width:12px;height:12px;border-radius:50%;background:var(--brand-red)}
.menu{display:flex;gap:11px;font-size:8px;font-weight:600;color:var(--white)}

.status-bar{height:14px;background:#f4f4f4;display:flex;justify-content:flex-end;gap:52px;padding-right:34px;align-items:center;font-size:6px;color:#333}

.hero{height:250px}
.hero-photo{position:absolute;inset:0;background:linear-gradient(110deg,#cfcfcf 0%,#8a8a8a 35%,#3a3a3a 65%,#181818 100%)}
.hero-content{position:absolute;left:0;right:0;top:100px;text-align:center}
.hero-title{font-size:21px;font-weight:700;color:var(--white);margin-left:40px}
.btn-hero{display:inline-flex;align-items:center;gap:6px;margin:12px 0 0 22px;background:var(--orange);color:var(--ink);font-size:12px;font-weight:600;padding:5px 16px}
.btn-hero .brand-dot{width:10px;height:10px}

.about{height:288px;background:var(--orange)}
.section-title{font-size:19px;font-weight:600;text-align:center}
.about .section-title{padding-top:36px}
.map-art{position:absolute;left:66px;top:84px;width:158px;height:160px;background:#4fc3dd}
.about-text{position:absolute;left:262px;top:104px;width:190px;font-size:7.4px;line-height:1.45}

.feature{display:flex;align-items:center}
.feature.grey{background:var(--light-grey)}
.feature h4,.plans h4{font-size:8.5px;font-weight:600;margin-bottom:6px}
.feature p,.plans .copy p{font-size:7.4px;line-height:1.35;width:230px}
.feature svg{position:absolute}
.f-help{height:156px}
.f-help .section-title{position:absolute;top:32px;left:0;right:0;font-size:11px}
.f-help .copy{position:absolute;left:224px;top:66px}
.f-help svg{left:74px;top:70px}
.f-access{height:146px}
.f-access .copy{position:absolute;left:74px;top:50px}
.f-access svg{left:374px;top:40px}
.f-protector{height:156px}
.f-protector .copy{position:absolute;left:224px;top:46px}
.f-protector svg{left:72px;top:48px}

.plans{height:416px}
.plans .copy{position:absolute;left:74px;top:54px}
.plans .devices{position:absolute;left:374px;top:48px}
.plans .section-title{position:absolute;top:162px;left:0;right:0;font-size:15px}
.plan{position:absolute;top:212px;width:142px;height:136px;border:2px solid var(--ink);text-align:center;background:var(--white)}
.plan.featured{top:202px;height:160px;width:144px}
.plan-term{font-family:"Tinos",serif;font-size:10px;margin-top:16px}
.plan-price{font-size:15px;font-weight:600;margin-top:6px}
.featured .plan-price{margin-top:16px}
.plan-btn{display:inline-block;margin-top:10px;border:1.5px solid var(--ink);font-size:9px;padding:1px 7px}
.featured .plan-btn{background:var(--green);border-color:var(--green);color:var(--white);margin-top:18px;padding:3px 8px}

.cta{height:168px;background:var(--orange);text-align:center}
.cta-quote{font-family:"Tinos",serif;font-size:10px;line-height:1.3;width:320px;margin:0 auto;padding-top:44px}
.btn-cta{display:inline-block;margin-top:10px;background:var(--cta-grey);color:var(--white);font-size:10px;font-weight:600;padding:5px 25px}
.cta-note{font-family:"Tinos",serif;font-size:8px;margin-top:3px}

.site-footer{height:218px;background:var(--footer);color:var(--white)}
.footer-cols{position:absolute;top:40px;left:112px;display:flex}
.footer-col{width:112px}
.footer-col h5{font-size:10px;font-weight:600;margin-bottom:10px}
.footer-col li{list-style:none;font-size:7.4px;line-height:1.9}
.copyright{position:absolute;top:154px;left:0;right:0;text-align:center;font-size:6.5px;font-weight:600}
.footer-rule{position:absolute;top:164px;left:40px;right:66px;border-top:1px solid #4c6565}
.social{position:absolute;top:178px;left:178px;display:flex;gap:10px}
.social span{width:21px;height:21px;background:var(--white);border-radius:3px}
.to-top{position:absolute;right:20px;top:174px}
</style>
</head>
<body>
<main class="page">
  <header class="nav">
    <div class="brand"><span class="brand-dot"></span>BRISKVPN</div>
    <nav class="menu"><span>Home</span><span>Features</span><span>VPN Apps</span><span>Pricing</span><span>Support Center</span></nav>
  </header>
  <div class="status-bar"><span>Your ISP:</span><span>Your IP:</span><span>Your location:</span><span>Your Status:</span></div>

  <section class="hero">
    <div class="hero-photo" role="img" aria-label="Black and white photo of a person using a laptop on a sofa"></div>
    <div class="hero-content">
      <h1 class="hero-title">The Complete VPN Solution</h1>
      <a class="btn-hero"><span class="brand-dot"></span>GET BRISK VPN</a>
    </div>
  </section>

  <section class="about">
    <h2 class="section-title">About VPN</h2>
    <div class="map-art" role="img" aria-label="Illustration of a folded world map with location pins and a compass"></div>
    <p class="about-text">Lorem ipsum dolor sit amet, consectetur adipiscing elit, sed do eiusmod tempor incididunt ut labore et dolore magna aliqua. Ut enim ad minim veniam, quis nostrud exercitation ullamco laboris nisi ut aliquip ex ea commodo consequat. Duis aute irure dolor in reprehenderit in voluptate velit esse cillum dolore eu fugiat nulla pariatur.</p>
  </section>

  <section class="feature grey f-help">
    <h2 class="section-title">How Does A VPN Help?</h2>
    <svg width="66" height="34" viewBox="0 0 66 34" fill="none" stroke="#f9a100" stroke-width="4"><path d="M4 14h24l-3 14H8z M38 14h24l-3 14H42z M28 18q5-4 10 0 M8 14l6-10 M58 14l-6-10"/></svg>
    <div class="copy"><h4>Hide Your IP.</h4><p>Lorem ipsum dolor sit amet, consectetur adipiscing elit, sed do eiusmod tempor incididunt ut labore et dolore magna aliqua. Ut</p></div>
  </section>

  <section class="feature f-access">
    <div class="copy"><h4>Access Websites.</h4><p>Lorem ipsum dolor sit amet, consectetur adipiscing elit, sed do eiusmod tempor incididunt ut labore et dolore magna aliqua. Ut</p></div>
    <svg width="58" height="58" viewBox="0 0 58 58" fill="none" stroke="#f9a100" stroke-width="2.5"><rect x="4" y="4" width="46" height="34"/><path d="M4 12h46 M20 20l-5 5 5 5 M34 20l5 5-5 5 M30 18l-6 14 M27 38v8 M16 48h22"/><circle cx="46" cy="46" r="7"/></svg>
  </section>

  <section class="feature grey f-protector">
    <svg width="54" height="64" viewBox="0 0 54 64"><path d="M4 8 27 2l23 6v22c0 16-10 26-23 32C14 56 4 46 4 30z" fill="none" stroke="#f9a100" stroke-width="5"/><path d="M27 2v60C14 56 4 46 4 30V8z" fill="#f9a100"/></svg>
    <div class="copy"><h4>Online Protector.</h4><p>Lorem ipsum dolor sit amet, consectetur adipiscing elit, sed do eiusmod tempor incididunt ut labore et dolore magna aliqua. Ut</p></div>
  </section>

  <section class="plans">
    <div class="copy"><h4>Protect all your Devices.</h4><p>Lorem ipsum dolor sit amet, consectetur adipiscing elit, sed do eiusmod tempor incididunt ut labore et dolore magna aliqua. Ut</p></div>
    <svg class="devices" width="62" height="58" viewBox="0 0 62 58" fill="none" stroke="#f9a100" stroke-width="3"><rect x="16" y="4" width="42" height="32"/><path d="M40 44h18"/><rect x="4" y="22" width="22" height="32" fill="#fff"/></svg>
    <h2 class="section-title">Choose Our Plan.</h2>
    <div class="plan" style="left:36px"><p class="plan-term">1 Month</p><p class="plan-price">$19.10</p><span class="plan-btn">GET PLAN</span></div>
    <div class="plan featured" style="left:185px"><p class="plan-term">2 Years</p><p class="plan-price">$20.14</p><span class="plan-btn">GET PLAN</span></div>
    <div class="plan" style="left:336px"><p class="plan-term">3 Years</p><p class="plan-price">$25.11</p><span class="plan-btn">GET PLAN</span></div>
  </section>

  <section class="cta">
    <p class="cta-quote">"Lorem ipsum dolor sit amet, consectetur adipiscing elit, sed do eiusmod tempor incididunt ut labore et dolore magna aliqua. Ut enim ad minim veniam, quis nostrud exercitation ullamco laboris</p>
    <a class="btn-cta">GET BRISK VPN</a>
    <p class="cta-note">Download Free Trial</p>
  </section>

  <footer class="site-footer">
    <div class="footer-cols">
      <div class="footer-col"><h5>APPS</h5><ul><li>Desktop VPN</li><li>Phone VPN</li><li>Tablet VPN</li><li>Other Devices</li></ul></div>
      <div class="footer-col"><h5>ABOUT</h5><ul><li>About Brisk</li><li>Blog</li><li>Review</li><li>Careers</li></ul></div>
      <div class="footer-col"><h5>SUPPORT</h5><ul><li>Help &amp; FAQ</li><li>Chat With Us</li><li>Press Area</li></ul></div>
    </div>
    <p class="copyright">Copyright © 2018. All rights reserved.</p>
    <div class="footer-rule"></div>
    <div class="social"><span></span><span></span><span></span><span></span><span></span></div>
    <svg class="to-top" width="14" height="10" viewBox="0 0 14 10" fill="none" stroke="#f9a100" stroke-width="3"><path d="M2 8l5-5 5 5"/></svg>
  </footer>
</main>
</body>
</html>
```